Volunteer Marketplace Needs New Look - www.Brimsey.org

Brimsey is the first online marketplace that lets you buy or sell volunteered services to raise money for charity. (www.Brimsey.org)

We went into live testing a few months ago to get some feedback and feel we need to redo the design. Some points:

- The current design was developed when a previous logo was being used. We later developed the current logo (which we love) and have never felt it really fit into the design. A design that plays up the logo would be great but not required.

- The circles in the logo represent coins which is a theme we are using in our branding (our business cards are coins). The marketplace offers a new form of currency people can use to give back. We don't feel the design should center around this concept, but a small element would be a nice touch.

We want a design that is engaging and fun - but still professional and credible.
Updates

I just want to thank you all for submitting designs. I have been trying to send feedback to everyone and am starting to eliminate designs so I can begin to narrow it. It is so hard to decide. You all did a great job! 

Target Market(s)

There are three target audiences - volunteers donating their services, customers buying donated services, and charities joining the program.

Industry/Entity Type

Business

Requirements
Must have
• - We feel we need to represent on the home page the concept of there being two parties that are coming together - the Volunteer and the Customer.

- We have a 60 second overview video in the works that we would like displayed on the home page.
Nice to have
• Incase it is helpful, here are some designs we like - but please know we are looking for creative ideas. Your design does not have to look like these.

http://www.lendora.org/
https://www.taskwell.com/
http://www.layoutbarn.com/website-templates/40056.html
http://www.layoutbarn.com/website-templates/40121.html
http://www.craftpool.com/

Also - please be creative about what content we put on our home page. We want to modernize the site. We can feed in our blog, twitter, facebook, etc into the home page if you think we should. We need your expertise to recommend what we need to showcase.
Should not have
• Please note that the paragraphs of content do not have to be on the home page. These are there now, but feedback tells us it is too boring - and they is why we are having the video done. So - you do not have to make room for all that text.

```html
<!DOCTYPE html>
<html lang="en">
<head>
<meta charset="utf-8">
<title>Brimsey – The new way to give</title>
<link href="https://fonts.googleapis.com/css2?family=Arimo:wght@400;700&display=swap" rel="stylesheet">
<style>
:root{
  --lime:#c5dd63;
  --slate:#566270;
  --teal:#14a99b;
  --teal-deep:#357b8c;
  --sky:#4a8fb0;
  --yellow:#f3ee7a;
  --white:#ffffff;
  --red:#e3131b;
}
*{box-sizing:border-box;margin:0;padding:0}
html,body{width:1200px;height:1000px;overflow:hidden}
body{background:var(--lime);font-family:"Arimo",Arial,sans-serif;position:relative}
.page{position:absolute;left:128px;top:0;width:930px;height:1000px;background:var(--slate);border-left:1px solid #333;border-right:1px solid #333}
.header{position:absolute;left:128px;top:0;width:930px;height:262px}
.header-bg{position:absolute;left:0;top:0}
.brand{position:absolute;left:162px;top:22px}
.brand-name{display:flex;align-items:center;gap:12px;font-size:64px;font-weight:700;color:var(--teal-deep);letter-spacing:1px;line-height:1}
.brand-dot{width:30px;height:30px;border-radius:50%;background:var(--teal)}
.tagline{margin-top:24px;margin-left:92px;font-size:23px;color:var(--slate)}
.account-bar{position:absolute;left:777px;top:0;width:265px;height:27px;background:var(--slate);border-radius:0 0 8px 8px;color:var(--white);font-size:11px;display:flex;justify-content:space-between;align-items:center;padding:0 10px}
.intro{position:absolute;left:535px;top:49px;width:500px;color:var(--white);font-size:12.5px;line-height:15px}
.intro a{color:var(--yellow)}
.intro p+p{margin-top:12px}
.search{display:flex;align-items:center;gap:6px}
.search input{width:231px;height:22px;border:1px solid #888;background:#fff}
.search button{width:84px;height:22px;margin-left:-6px;border:0;background:var(--slate);color:#fff;font:12.5px "Arimo",sans-serif}
.nav-item{position:absolute;display:flex;align-items:center;gap:12px;color:var(--white);font-size:20px;line-height:24px}
.play-ring{width:39px;height:39px;flex:none}
.feature{position:absolute;left:120px;top:258px;width:950px;height:314px;background:var(--white);border:3px solid var(--slate)}
.bubble{position:absolute;left:31px;top:34px;width:229px;height:76px;background:var(--teal);border-radius:18px;color:#fff;font-size:15.5px;line-height:19px;text-align:center;padding-top:19px}
.bubble::after{content:"";position:absolute;left:184px;bottom:-20px;border-left:6px solid transparent;border-right:12px solid transparent;border-top:22px solid var(--teal)}
.people{position:absolute;left:8px;top:130px;width:276px;height:178px;background:linear-gradient(180deg,#fff,#f1f1f1)}
.video{position:absolute;left:284px;top:18px;width:374px;height:272px;background:var(--slate);display:flex;align-items:center;justify-content:center}
.share{position:absolute;left:757px;top:8px;display:flex;align-items:center;gap:9px;font-size:12px;color:#333}
.share span.icon{width:19px;height:19px;border-radius:3px;background:var(--sky)}
.share span.icon.green{background:#2e8b3a}
.share span.icon.mail{background:#ddd}
.help{position:absolute;left:684px;top:38px;width:244px;text-align:center;color:var(--teal)}
.help-big{font-size:84px;font-weight:700;line-height:74px}
.help-sub{font-size:36px;font-weight:700;line-height:40px}
.charity-grid{position:absolute;left:700px;top:158px;display:grid;grid-template-columns:92px 92px;column-gap:21px;row-gap:5px}
.charity-badge{height:32px;display:flex;align-items:center;gap:6px}
.charity-badge i{width:30px;height:30px;border-radius:50%;background:var(--red)}
.charity-badge b{width:54px;height:16px;background:#ececec;border-radius:2px}
.join{position:absolute;left:690px;top:245px;width:212px;height:43px;background:var(--slate);border-radius:7px;color:#fff;font-size:33px;font-weight:700;text-align:center;line-height:43px}
.concept{position:absolute;left:145px;top:592px;width:615px;color:var(--white)}
.concept h1{font-size:20px;font-weight:700;margin-bottom:28px}
.concept p{font-size:11.6px;line-height:23.3px;margin-bottom:23px}
.photo{position:absolute;left:791px;width:242px;box-shadow:4px 4px 5px rgba(0,0,0,.45)}
.photo.kids-laptop{top:599px;height:182px;background:linear-gradient(160deg,#f3a43a,#e86a18)}
.photo.kids-field{top:804px;height:176px;background:linear-gradient(160deg,#6fb43c,#3f8a27)}
</style>
</head>
<body>
<div class="page"></div>

<header class="header">
  <svg class="header-bg" width="930" height="262" viewBox="0 0 930 262">
    <rect width="930" height="262" fill="#ffffff"/>
    <path d="M390 0 C 360 70 370 150 440 200 L 930 200 L 930 0 Z" fill="var(--teal)"/>
    <path d="M0 200 C 90 155 260 150 340 198 L 300 262 L 0 262 Z" fill="var(--slate)"/>
    <path d="M262 262 C 340 185 520 150 680 196 L 610 262 Z" fill="var(--teal-deep)"/>
    <path d="M580 262 C 680 170 820 150 930 160 L 930 262 Z" fill="var(--sky)"/>
  </svg>

  <div class="nav-item" style="left:53px;top:197px">
    <svg class="play-ring" viewBox="0 0 40 40"><circle cx="20" cy="20" r="18" fill="none" stroke="#fff" stroke-width="2.5"/><path d="M15 11 L29 20 L15 29 Z" fill="#fff"/></svg>
    <span>Search<br>Donated Services</span>
  </div>
  <div class="nav-item" style="left:376px;top:197px">
    <svg class="play-ring" viewBox="0 0 40 40"><circle cx="20" cy="20" r="18" fill="none" stroke="#fff" stroke-width="2.5"/><path d="M15 11 L29 20 L15 29 Z" fill="#fff"/></svg>
    <span>Search<br>Help Wanted Ads</span>
  </div>
  <div class="nav-item" style="left:700px;top:197px">
    <svg class="play-ring" viewBox="0 0 40 40"><circle cx="20" cy="20" r="18" fill="none" stroke="#fff" stroke-width="2.5"/><path d="M15 11 L29 20 L15 29 Z" fill="#fff"/></svg>
    <span>How It Works</span>
  </div>
</header>

<div class="brand">
  <div class="brand-name"><span>Brimsey</span><span class="brand-dot"></span></div>
  <div class="tagline">The new way to give.</div>
</div>

<div class="account-bar"><span>Welcome Guest</span><span>Log in &nbsp;|&nbsp; Register</span></div>

<div class="intro">
  <p>I want to list my talent! Have a talent you would like to donate to help raise money for those in need? <a href="#">Create My Volunteer Profile »</a></p>
  <p>I want to hire donated talent! Looking for an artist, need a music lesson, searching for a handy man?</p>
  <div class="search"><span>Search donated talent:</span><input type="text" aria-label="Search donated talent"><button>Submit</button></div>
</div>

<section class="feature">
  <div class="bubble">Watch 60 second overview<br>video in the works</div>
  <div class="people" role="img" aria-label="Hand-drawn volunteer and customer waving to each other"></div>
  <div class="video" role="img" aria-label="Overview video player">
    <svg width="130" height="130" viewBox="0 0 130 130"><circle cx="65" cy="65" r="60" fill="none" stroke="#fff" stroke-width="6"/><path d="M48 32 L100 65 L48 98 Z" fill="#fff"/></svg>
  </div>
  <div class="share"><span>Share</span><span class="icon green"></span><span class="icon"></span><span class="icon"></span><span class="icon"></span><span class="icon mail"></span></div>
  <div class="help"><div class="help-big">HELP</div><div class="help-sub">any Charity!</div></div>
  <div class="charity-grid">
    <div class="charity-badge"><i></i><b></b></div>
    <div class="charity-badge"><i></i><b></b></div>
    <div class="charity-badge"><i></i><b></b></div>
    <div class="charity-badge"><i></i><b></b></div>
  </div>
  <div class="join">Join Us!</div>
</section>

<main class="concept">
  <h1>THE CONCEPT...</h1>
  <p>JUST LAUNCHED! Brimsey is hot off the press! Welcome to our first visitors.</p>
  <p>Most people want to make a difference, but getting involved with the cause you care about can be a challenge. That's how Brimsey changes the world of giving!</p>
  <p>Everyone has talents - some professional and some hobbies. Lots of people and companies need people with talent. Brimsey enables those with talent to volunteer their time to those who need to hire people with skills -- while benefiting the charity of your choice.</p>
  <p>Whether you are a landscaper, hairdresser, mechanic, musician, computer programmer, and much more -- if you or your business can perform services people will pay for -- you can volunteer your services for hire and have the payment go to charity.</p>
  <p>Not only can you volunteer your time but by hiring volunteered talent such as babysitters, house cleaners, and more you are spending as you normally would but now you are using your money to change the world!</p>
</main>

<div class="photo kids-laptop" role="img" aria-label="Photo of children lying on an orange mat around a laptop"></div>
<div class="photo kids-field" role="img" aria-label="Photo of two smiling children in a green field"></div>
</body>
</html>
```